Fintech company needs ads created around "can't afford help"

Design 3 ads (total) that focus around HELPING people who can't afford to get help with their finances.

The 3 ads will be made up of 1 design for each audience:
• Millennial
• Generation X
• Baby Boomer

We are testing campaigns in Chirpwall that will drive to a landing page. We are an online financial-tech company who helps people manage their retirement account. We’re looking for creative talent who are effective at developing imagery to be used in Chirpwall to grab people’s attention and drive clicks. Because of the scrutiny in our industry, we’ll handle the ad copy above and below the imagery you create. We encourage you to use/not use words in your creative.

Target Market(s)

• Millennial
• Generation X
• Baby Boomer

Industry/Entity Type

Financial Service

Requirements
Must have
• Image Dimensions
• Width: 1200 Height: 628
• Final PSD Designs
• Feel free to play around with any color scheme.
• Tasteful – we are not a traditional, stodgy Linden Row Financial firm, but we need to convey that we are trustworthy and legitimate.
Nice to have
• You are not limited to photos – whatever you believe will stand out and engage with prospective clients is fair game (including illustrations, animation, video, etc).
• Think about how your work could translate into other forms such as motion graphics or video.
• Ultimately, we will test our favorites and come back to those with the highest performance which will turn into additional work and additional formats.
Should not have
• • No stock photography UNLESS found at Pixanta (we will pay for the image)
• • No Testimonials – regulations prevent us from using testimonials in our advertisements

```html
<!DOCTYPE html>
<html lang="en">
<head>
<meta charset="utf-8">
<title>Financial Help Ads – Three Audiences</title>
<link rel="stylesheet" href="https://fonts.googleapis.com/css2?family=Arimo:wght@700&display=swap">
<style>
  :root {
    --page-bg: #ffffff;
    --panel-blue: #1b4689;
    --panel-blue-dark: #163a75;
    --headline-white: #f4f6f8;
    --headline-shadow: rgba(10, 20, 45, 0.85);
    --accent-cyan: #86eef4;
    --label-ink: #111111;
    --frame-line: #3a3a3a;
  }
  html, body {
    margin: 0;
    padding: 0;
    width: 818px;
    height: 1200px;
    overflow: hidden;
    background: var(--page-bg);
    font-family: "Arimo", Arial, sans-serif;
  }
  .sheet {
    position: relative;
    width: 818px;
    height: 1200px;
  }
  .ad {
    position: absolute;
    left: 100px;
    width: 653px;
    height: 342px;
    outline: 1px solid var(--frame-line);
    overflow: hidden;
  }
  .ad--boomer { top: 34px; }
  .ad--genx { top: 422px; }
  .ad--millennial { top: 818px; }
  .ad__art {
    position: absolute;
    inset: 0;
    width: 653px;
    height: 342px;
  }
  .ad__headline {
    position: absolute;
    left: 17px;
    top: 51px;
    margin: 0;
    font-size: 23px;
    line-height: 26px;
    font-weight: 700;
    letter-spacing: 0.3px;
    color: var(--headline-white);
    text-shadow: 1px 1px 1px var(--headline-shadow), 0 0 2px var(--headline-shadow);
  }
  .ad__help {
    position: absolute;
    left: 23px;
    top: 175px;
    margin: 0;
    font-size: 23px;
    line-height: 26px;
    font-weight: 700;
    color: var(--accent-cyan);
    text-shadow: 1px 1px 1px rgba(10, 20, 45, 0.6);
  }
  .ad__expert {
    position: absolute;
    left: 50px;
    width: 200px;
    top: 228px;
    margin: 0;
    text-align: center;
    font-size: 23px;
    line-height: 26px;
    font-weight: 700;
    color: var(--accent-cyan);
    text-shadow: 1px 1px 1px rgba(10, 20, 45, 0.6);
  }
  .ad--genx .ad__help,
  .ad--millennial .ad__help { left: 18px; }
  .ad--genx .ad__expert,
  .ad--millennial .ad__expert { left: 45px; }
  .ad-label {
    position: absolute;
    left: 361px;
    margin: 0;
    font-family: Arial, Helvetica, sans-serif;
    font-size: 13px;
    color: var(--label-ink);
    white-space: pre;
  }
  .ad-label--boomer { top: 381px; }
  .ad-label--genx { top: 770px; }
  .ad-label--millennial { top: 1165px; }
</style>
</head>
<body>
<div class="sheet">

  <section class="ad ad--boomer">
    <svg class="ad__art" viewBox="0 0 653 342" aria-hidden="false">
      <defs>
        <linearGradient id="boomerPhoto" x1="0" y1="0" x2="1" y2="1">
          <stop offset="0" stop-color="#e8eef3"/>
          <stop offset="0.5" stop-color="#c9b8a6"/>
          <stop offset="1" stop-color="#8a7a70"/>
        </linearGradient>
        <radialGradient id="panelGlow" cx="0.1" cy="0" r="1">
          <stop offset="0" stop-color="var(--panel-blue-dark)"/>
          <stop offset="1" stop-color="var(--panel-blue)"/>
        </radialGradient>
      </defs>
      <rect x="260" y="0" width="393" height="342" fill="url(#boomerPhoto)" role="img" aria-label="Photo of a smiling retired couple, the husband reading a newspaper while his wife holds a wrapped gift"/>
      <path d="M0 0 H396 C 350 110, 325 245, 280 342 H0 Z" fill="url(#panelGlow)"/>
    </svg>
    <h2 class="ad__headline">THE SOLUTION OF<br>FINANCIAL PROBLEMS<br>ON YOUR RETIREMENT<br>AGE IS IN HERE</h2>
    <p class="ad__help">WE CAN HELP YOU!</p>
    <p class="ad__expert">WE ARE<br>THE EXPERT</p>
  </section>
  <p class="ad-label ad-label--boomer">1200x628     BABY BOOMER</p>

  <section class="ad ad--genx">
    <svg class="ad__art" viewBox="0 0 653 342">
      <defs>
        <linearGradient id="genxPhoto" x1="0" y1="0" x2="1" y2="1">
          <stop offset="0" stop-color="#ece6df"/>
          <stop offset="0.55" stop-color="#d8cfc6"/>
          <stop offset="1" stop-color="#7f93ad"/>
        </linearGradient>
        <radialGradient id="panelGlow2" cx="0.1" cy="0" r="1">
          <stop offset="0" stop-color="var(--panel-blue-dark)"/>
          <stop offset="1" stop-color="var(--panel-blue)"/>
        </radialGradient>
      </defs>
      <rect x="260" y="0" width="393" height="342" fill="url(#genxPhoto)" role="img" aria-label="Photo of two smiling middle-aged men sitting together on a sofa"/>
      <path d="M0 0 H396 C 350 110, 325 245, 280 342 H0 Z" fill="url(#panelGlow2)"/>
    </svg>
    <h2 class="ad__headline">IF YOU NEED TO<br>EXPAND YOUR BUSINESS<br>AND HAVE THE FINANCIAL<br>PROBLEMS</h2>
    <p class="ad__help">WE CAN HELP YOU!</p>
    <p class="ad__expert">WE ARE<br>THE EXPERT</p>
  </section>
  <p class="ad-label ad-label--genx">1200x628     GENERATION X</p>

  <section class="ad ad--millennial">
    <svg class="ad__art" viewBox="0 0 653 342">
      <defs>
        <linearGradient id="millennialPhoto" x1="0" y1="0" x2="1" y2="1">
          <stop offset="0" stop-color="#dfe3d2"/>
          <stop offset="0.5" stop-color="#d9c7a3"/>
          <stop offset="1" stop-color="#8c8f9c"/>
        </linearGradient>
        <radialGradient id="panelGlow3" cx="0.1" cy="0" r="1">
          <stop offset="0" stop-color="var(--panel-blue-dark)"/>
          <stop offset="1" stop-color="var(--panel-blue)"/>
        </radialGradient>
      </defs>
      <rect x="260" y="0" width="393" height="342" fill="url(#millennialPhoto)" role="img" aria-label="Photo of a worried young woman holding her forehead while a friend comforts her"/>
      <path d="M0 0 H396 C 350 110, 325 245, 280 342 H0 Z" fill="url(#panelGlow3)"/>
    </svg>
    <h2 class="ad__headline">THE MILLENIAL<br>GENERATIONS NEED<br>HELP ABOUT THEIR<br>FINANCIAL PROBLEMS</h2>
    <p class="ad__help">WE CAN HELP YOU!</p>
    <p class="ad__expert">WE ARE<br>THE EXPERT</p>
  </section>
  <p class="ad-label ad-label--millennial">1200x628     MILLENIAL</p>

</div>
</body>
</html>
```